I am looking for a Business Card Design for my spirit company titled "Harbor Pour Co" The company specializes in prohibition style/speakeasy mixology drinks and alcohol distribution. I am looking for Retro, Masculine, Sophisticated Card that embodies the look of Prohibition. Black and White colors. Also add Social Page, Instgram logo

Information that should go on the card is my Name, Title, Phone, Email, Website as follows:

Tobias K Verran
Principal
301.555.0187
tobias@harborpourco.example
harborpourco.example
Updates

Hello all I have uploaded a pdf version of the logo. It seems as if some are saying the resolution is too small.

Target Market(s)

Male and Female drinkers of all ages with a sophisticated palate that have an appreciation for fine crafted cocktail

Industry/Entity Type

Business

Requirements
Must have
• Information that should go on the card is my Name, Title, Phone, Email, Website as follows:

Tobias K Verran
Principal
301.555.0187
tobias@harborpourco.example
harborpourco.example

```html
<!DOCTYPE html>
<html lang="en">
<head>
<meta charset="utf-8">
<title>Harbor Pour Co — Business Card</title>
<link rel="stylesheet" href="https://fonts.googleapis.com/css2?family=Open+Sans:wght@400;600&display=swap">
<style>
  :root {
    --backdrop: #d9d6d1;
    --paper: #ebe9e5;
    --ink: #1b1a1a;
    --panel-text: #f2f1ee;
  }
  * { box-sizing: border-box; margin: 0; padding: 0; }
  html, body { width: 1200px; height: 926px; overflow: hidden; }
  body {
    background: var(--backdrop);
    font-family: "Open Sans", Arial, sans-serif;
    display: flex;
    flex-direction: column;
    align-items: center;
    justify-content: center;
    gap: 60px;
  }
  .card {
    position: relative;
    width: 640px;
    height: 366px;
    background: var(--paper);
    box-shadow: 0 6px 18px rgba(0,0,0,0.18);
  }
  .brand-name {
    position: absolute;
    font-family: "Open Sans", Arial, sans-serif;
    font-weight: 600;
    color: var(--ink);
    line-height: 1.05;
    text-align: center;
  }
  /* front */
  .card-front .brand-name {
    left: 26px;
    top: 96px;
    width: 220px;
    font-size: 40px;
  }
  .contact-panel {
    position: absolute;
    right: 22px;
    top: 24px;
    bottom: 24px;
    width: 350px;
    background: var(--ink);
    color: var(--panel-text);
    padding: 30px 28px;
  }
  .holder-name { font-size: 25px; font-weight: 400; line-height: 1.2; }
  .holder-title { font-size: 22px; font-weight: 400; margin-bottom: 16px; }
  .contact-list { list-style: none; }
  .contact-list li {
    display: flex;
    align-items: center;
    gap: 8px;
    font-size: 19px;
    line-height: 1.35;
    white-space: nowrap;
  }
  .contact-list svg { width: 13px; height: 13px; flex: none; }
  /* back */
  .card-back .brand-name {
    left: 0;
    right: 0;
    top: 148px;
    font-size: 58px;
  }
</style>
</head>
<body>
  <section class="card card-front">
    <div class="brand-name">Harbor<br>Pour Co</div>
    <div class="contact-panel">
      <p class="holder-name">Tobias K Verran</p>
      <p class="holder-title">Principal</p>
      <ul class="contact-list">
        <li>
          <svg viewBox="0 0 13 13" aria-hidden="true"><rect x="1" y="1" width="11" height="11" rx="1.5" fill="var(--panel-text)"/><path d="M4 3.5c0 3 2.5 5.5 5.5 5.5l.5-1.5-1.7-.8-.7.8C6.6 7 6 6.4 5.5 5.4l.8-.7-.8-1.7z" fill="var(--ink)"/></svg>
          301.555.0187
        </li>
        <li>
          <svg viewBox="0 0 13 13" aria-hidden="true"><rect x="1" y="2.5" width="11" height="8" fill="none" stroke="var(--panel-text)" stroke-width="1.2"/><path d="M1 3l5.5 4.2L12 3" fill="none" stroke="var(--panel-text)" stroke-width="1.2"/></svg>
          tobias@harborpourco.example
        </li>
        <li>
          <svg viewBox="0 0 13 13" aria-hidden="true"><circle cx="6.5" cy="6.5" r="5.3" fill="none" stroke="var(--panel-text)" stroke-width="1.1"/><ellipse cx="6.5" cy="6.5" rx="2.3" ry="5.3" fill="none" stroke="var(--panel-text)" stroke-width="1"/><path d="M1.2 6.5h10.6" stroke="var(--panel-text)" stroke-width="1"/></svg>
          harborpourco.example
        </li>
        <li>
          <svg viewBox="0 0 13 13" aria-hidden="true"><rect x="2" y="2" width="9" height="9" fill="var(--panel-text)"/></svg>
          Social Page
        </li>
        <li>
          <svg viewBox="0 0 13 13" aria-hidden="true"><rect x="2" y="2" width="9" height="9" fill="var(--panel-text)"/></svg>
          Photo Feed
        </li>
      </ul>
    </div>
  </section>

  <section class="card card-back">
    <div class="brand-name">Harbor Pour Co</div>
  </section>
</body>
</html>
```